Presentation and Communication Coaching Services Business needs updated interactive web site

I want to keep the color scheme, functionality, and pages of my current site, but with a newer/updated look. I need to improve security and simplify images, etc. (Please see current site http://brackwellvoicetutor.com ) This will need be functional on mobile devices, as well.

I'm attached to the scrolling client list and scrolling client feedback.

Industry/Entity Type

Professional Service

Font styles to use
Sans Serif

Colors
0356a4
f37122
33a6d7

Requirements
Must have
• scrolling client banner on home page, client comments slider, color scheme
• Please see current site: http://brackwellvoicetutor.com
Nice to have
• better action/appearance
Should not have
• I don't want it to look like all the other sites/templates

```html
<!DOCTYPE html>
<html lang="en">
<head>
<meta charset="utf-8">
<title>Brackwell Voice Tutoring</title>
<link href="https://fonts.googleapis.com/css2?family=Raleway:ital,wght@0,400;0,500;0,600;0,700;1,400&display=swap" rel="stylesheet">
<style>
:root{
  --navy:#0d3449;
  --teal-mid:#174c66;
  --gold:#e6ad3b;
  --gold-text:#f2b53c;
  --white:#ffffff;
  --muted:#c3d5dd;
  --accent:#33a6d7;
  --brand-red:#d94a3c;
  --footbar:#0c2f42;
}
*{box-sizing:border-box;margin:0;padding:0}
html,body{width:1200px;height:3120px;overflow:hidden}
body{font-family:"Raleway",sans-serif;color:var(--white);
  background:linear-gradient(180deg,#0f3f57 0%,#164e68 20%,#1a5a76 45%,#1a5674 62%,#134760 80%,#0e3a50 100%);position:relative}
.abs{position:absolute}
/* header */
.logo{left:150px;top:22px;font-size:26px;font-weight:600;letter-spacing:-.3px}
.logo span{color:var(--gold-text)}
.social{display:flex;gap:10px}
.social i{display:block;width:30px;height:30px;border-radius:50%;border:2px solid #5f8ea3;background:rgba(255,255,255,.05)}
.social i.on{background:var(--accent);border-color:var(--accent)}
.header-social{left:563px;top:22px}
.btn{display:inline-block;border-radius:18px;font-size:12px;font-weight:700;text-align:center;line-height:32px;height:32px}
.btn-gold{background:var(--gold);color:#233}
.btn-blue{background:var(--accent);color:var(--white)}
.nav{left:150px;top:82px;width:900px;display:flex;justify-content:space-between;font-size:11px;font-weight:700;letter-spacing:.6px}
.nav a{color:var(--white);text-decoration:none}
.nav a.active{color:var(--accent)}
/* hero */
.hero-photo{left:40px;top:320px;width:420px;height:520px;border-radius:8px;
  background:radial-gradient(ellipse at 50% 40%,rgba(150,170,180,.35),rgba(20,60,80,0) 70%)}
.mic-photo{left:470px;top:140px;width:260px;height:200px;border-radius:50%;
  background:radial-gradient(circle,rgba(120,150,165,.35),rgba(20,60,80,0) 70%)}
.quote{left:300px;top:228px;width:600px;text-align:center;font-style:italic;font-size:18px;line-height:26px;color:#e5eef2}
.quote b{color:var(--accent);font-weight:700}
.dots{left:565px;top:391px;display:flex;gap:6px}
.dots i{width:9px;height:9px;border-radius:50%;border:1.5px solid #8fb0bf}
.hero-title{left:637px;top:486px;font-size:29px;line-height:34px;color:var(--gold-text);font-weight:500}
.hero-text{left:637px;top:568px;width:420px;font-size:12.5px;line-height:18px;color:#e2ecf0}
.hero-text p+p{margin-top:16px}
/* register band */
.band{left:0;top:843px;width:1200px;height:114px;background:var(--gold)}
.band-title{left:150px;top:880px;width:420px;font-size:16.5px;font-weight:700;color:#1f2b33;line-height:20px}
.band-form{left:600px;top:876px;width:450px;height:46px;border-radius:23px;border:2px solid #1a4a63;background:rgba(255,255,255,.08)}
.band-form span{position:absolute;left:24px;top:13px;font-size:13px;color:#2d4653}
.band-form .btn{position:absolute;right:-2px;top:-2px;height:46px;line-height:46px;width:180px;border-radius:23px;background:#143f57;color:var(--white);font-size:13px}
/* features */
.feature-photo{left:700px;top:960px;width:380px;height:360px;
  background:radial-gradient(ellipse at 50% 40%,rgba(150,170,180,.25),rgba(20,60,80,0) 70%)}
.feature{width:240px;text-align:center}
.feature .ic{width:112px;height:112px;border-radius:50%;background:var(--gold);margin:0 auto;display:flex;align-items:center;justify-content:center}
.feature .ic.white{background:var(--white)}
.feature h3{margin-top:30px;font-size:17px;font-weight:700}
.feature h3.gold{color:var(--gold-text)}
.feature p{margin:10px auto 0;width:200px;font-size:12px;line-height:18px;color:#dce8ed}
/* services */
.section-title{left:0;width:1200px;text-align:center;font-size:27px;color:var(--gold-text);font-weight:500}
.service{width:330px;font-size:12px;line-height:18px;color:var(--muted)}
.service h4{font-size:17px;color:var(--white);font-weight:700;margin-bottom:8px}
.service.right{text-align:right}
.service.hl{background:linear-gradient(90deg,var(--teal-mid),rgba(23,76,102,.5));border-left:4px solid var(--gold);padding:14px 20px}
.service.hl h4{color:var(--gold-text)}
.ring{left:475px;top:1440px;width:250px;height:250px;border-radius:50%;border:2px solid rgba(255,255,255,.55)}
.ring-inner{left:490px;top:1455px;width:220px;height:220px;border-radius:50%;background:#1e6380;text-align:center;padding-top:78px}
.ring-inner .n1{font-size:40px;font-weight:500;line-height:40px}
.ring-inner .n2{font-size:20px;color:var(--accent)}
/* clients */
.clients{left:150px;top:1781px;width:900px;display:flex;justify-content:space-between}
.client{width:170px;height:77px;background:var(--navy);display:flex;align-items:center;justify-content:center;gap:8px;font-size:19px;font-weight:700;color:var(--brand-red);white-space:nowrap}
.client .sq{width:16px;height:16px;background:var(--brand-red)}
/* publications */
.pub{width:240px;text-align:center}
.pub .frame{height:300px;display:flex;align-items:flex-end;justify-content:center}
.pub .cover{width:180px;height:300px;box-shadow:6px 8px 14px rgba(0,0,0,.35)}
.pub p{margin-top:24px;font-size:13px;line-height:17px;font-weight:600}
/* tools */
.sub{left:0;top:2463px;width:1200px;text-align:center;font-size:14px}
.sub b{color:var(--accent);font-weight:500}
.tools{left:150px;top:2535px;width:410px;list-style:none;font-size:12px;line-height:22.5px}
.tools li{display:flex;align-items:flex-start;gap:12px}
.tools svg{flex:none;margin-top:5px}
.video{left:601px;top:2517px;width:450px;height:300px;background:linear-gradient(135deg,#9c6b4c,#c8a689 45%,#7d4f3a)}
.play{left:801px;top:2642px}
/* footer */
.f-name{left:150px;top:2900px;font-size:27px;color:var(--gold-text);font-weight:500}
.f-role{left:150px;top:2940px;font-size:13px}
.f-text{left:150px;top:2972px;width:420px;font-size:12px;line-height:18px;color:var(--muted)}
.f-contact{left:639px;top:2918px;width:135px;height:28px;line-height:28px;font-size:11px}
.f-info{left:639px;top:2962px;width:410px;display:flex;justify-content:space-between;font-size:13px;font-weight:700}
.f-social{left:639px;top:2998px}
.f-reg{left:839px;top:2997px;width:135px}
.to-top{left:1112px;top:2905px}
.footbar{left:0;top:3075px;width:1200px;height:45px;background:var(--footbar);font-size:11px;color:#9fb8c3}
.footbar .c{position:absolute;left:150px;top:16px}
.footbar .l{position:absolute;right:150px;top:16px}
</style>
</head>
<body>

<header>
  <div class="abs logo">brackwell<span>voicetutoring</span></div>
  <div class="abs social header-social"><i></i><i class="on"></i><i></i><i></i><i></i></div>
  <a class="abs btn btn-gold" style="left:765px;top:22px;width:135px">Register Now!</a>
  <a class="abs btn btn-blue" style="left:917px;top:22px;width:135px">Client Login</a>
  <nav class="abs nav">
    <a class="active">HOME</a><a>ABOUT</a><a>CLIENTS</a><a>REVIEWS</a><a>SERVICES</a><a>CONTACT</a><a>SPEAKING SECRETS</a>
  </nav>
</header>

<section class="hero">
  <div class="abs mic-photo" role="img" aria-label="Faint photo of a stage microphone"></div>
  <div class="abs hero-photo" role="img" aria-label="Photo of a woman presenting with a microphone"></div>
  <blockquote class="abs quote"><b>“</b> I was the first to present and they were really interested in some of the key stuff; they were throwing questions left/right. Ended up being up on the stage for 1 hour and 10 min! It was really great! <b>”</b></blockquote>
  <div class="abs dots"><i></i><i></i><i></i><i></i><i></i></div>
  <h1 class="abs hero-title">You're good at what you do.<br>Learn How to let it show.</h1>
  <div class="abs hero-text">
    <p>An individual works hard to reach a place of respect and authority in her or his chosen profession. Effective self-presentation adds confidence and allows one's unique personality and expertise to shine through – in fact, it is key in separating from the pack and reaching higher goals. As competition increases, these skills become more essential in demonstrating value to an employer, manager, or board.</p>
    <p>You've done your best to reach this professional level. It's time to develop what it takes to reach the next one.</p>
  </div>
</section>

<section>
  <div class="abs band"></div>
  <div class="abs band-title">Register and receive FREE "7 Habits That Mute<br>Your Message"</div>
  <div class="abs band-form"><span>name@email.com</span><a class="btn">Register Now!</a></div>
</section>

<section>
  <div class="abs feature-photo" role="img" aria-label="Faint photo of a young woman speaking"></div>
  <div class="abs feature" style="left:142px;top:1057px">
    <div class="ic"><svg width="46" height="46" viewBox="0 0 24 24" fill="#fff"><path d="M6 3h12v3h3v3a4 4 0 0 1-4 4h-.4A5 5 0 0 1 13 16v3h3v2H8v-2h3v-3a5 5 0 0 1-3.6-3H7a4 4 0 0 1-4-4V6h3zm-1 5v1a2 2 0 0 0 2 2V8zm14 0h-2v3a2 2 0 0 0 2-2z"/></svg></div>
    <h3>The Goal</h3>
  </div>
  <div class="abs feature" style="left:367px;top:1057px">
    <div class="ic white"><svg width="50" height="50" viewBox="0 0 24 24" fill="#e6ad3b"><path d="M11 2h2v3h7l2 2-2 2h-7v2h-7l-2-2 2-2h7V7H4z"/><rect x="11" y="11" width="2" height="11"/></svg></div>
    <h3 class="gold">The Challenge</h3>
    <p>Find a path to develop skills and strategies to accomplish this aim while also projecting confidence, warmth, and credibility.</p>
  </div>
  <div class="abs feature" style="left:593px;top:1057px">
    <div class="ic"><svg width="46" height="46" viewBox="0 0 24 24" fill="#fff"><path d="M10 2h4l.5 3 2 1 2.5-1.8 2.8 2.8L20 9.5l1 2 3 .5v4l-3 .5-1 2 1.8 2.5-2.8 2.8L16.5 22l-2 1-.5 3h-4l-.5-3-2-1-2.5 1.8-2.8-2.8L4 18.5l-1-2-3-.5v-4l3-.5 1-2-1.8-2.5L5 4.2 7.5 6l2-1zM12 9a3 3 0 1 0 0 6 3 3 0 0 0 0-6z" transform="scale(.85) translate(2 0)"/></svg></div>
    <h3>The Solution</h3>
  </div>
  <div class="abs feature" style="left:818px;top:1057px">
    <div class="ic"><svg width="48" height="48" viewBox="0 0 24 24" fill="none" stroke="#fff" stroke-width="2"><path d="M3 3v18h18"/><path d="M6 16l4-5 3 3 6-7"/><path d="M15 7h4v4"/></svg></div>
    <h3>The Result</h3>
  </div>
</section>

<section>
  <h2 class="abs section-title" style="top:1376px">Services We Provide</h2>
  <div class="abs service right hl" style="left:150px;top:1464px;width:320px">
    <h4>01. Coaching</h4>
    One-on-one, individual and customized to your unique goals, obstacles, and challenges. In person, or via video conference.
  </div>
  <div class="abs service right" style="left:120px;top:1590px;width:330px">
    <h4>02. Custom Workshops</h4>
    Unique, effective program design &amp; facilitation to match the needs of executives, managers, or promising individuals ...
  </div>
  <div class="abs service" style="left:750px;top:1474px">
    <h4>03. Accents</h4>
    Support for executives from outside the U.S. to increase intelligibility &amp; diminish obstacles to successful communication ...
  </div>
  <div class="abs service" style="left:750px;top:1590px">
    <h4>04. Keynote Speeches</h4>
    Fresh ways of thinking about speaking and communication combined with practical tools for participants of your next conference ...
  </div>
  <div class="abs ring"></div>
  <div class="abs ring-inner"><div class="n1">brackwell</div><div class="n2">voicetutoring</div></div>
</section>

<section class="abs clients">
  <div class="client"><span class="sq"></span>Halvorn</div>
  <div class="client">Pelta</div>
  <div class="client">Marrow &amp; Finch</div>
  <div class="client"><span class="sq"></span>Northgate</div>
  <div class="client">Q24</div>
</section>

<section>
  <h2 class="abs section-title" style="top:1924px">Recent Publications</h2>
  <div class="abs pub" style="left:247px;top:1986px">
    <div class="frame"><div class="cover" style="background:linear-gradient(160deg,#3aa8d4,#1d6f93 60%,#0d3c52)" role="img" aria-label="Magazine cover, Harbor Blue Style Book"></div></div>
    <p>Spring/Summer Harbor<br>Blue Style Book</p>
  </div>
  <div class="abs pub" style="left:480px;top:1986px">
    <div class="frame"><div class="cover" style="background:linear-gradient(160deg,#7fc6e6,#c7dde6 50%,#4d8fb0)" role="img" aria-label="Magazine cover, Maison Claret"></div></div>
    <p>Maison Claret<br>Magazine</p>
  </div>
  <div class="abs pub" style="left:706px;top:1986px">
    <div class="frame"><div class="cover" style="width:224px;height:270px;background:linear-gradient(180deg,#a8362c,#6c2a24 60%,#2b2826)" role="img" aria-label="Newspaper photo of a man facing press microphones"></div></div>
    <p>Metro Ledger<br>Post</p>
  </div>
</section>

<section>
  <h2 class="abs section-title" style="top:2412px">BVT Provides Training, Tools, and Techniques</h2>
  <p class="abs sub">Watch A <b>Free Video</b> With 5 Great Speaking Tips</p>
  <ul class="abs tools">
    <li><svg width="12" height="12" viewBox="0 0 12 12"><circle cx="6" cy="6" r="5" fill="none" stroke="#e6ad3b" stroke-width="1.3"/><path d="M3.5 6l1.8 1.8L8.6 4.3" fill="none" stroke="#e6ad3b" stroke-width="1.3"/></svg>Executive Presence – Polishing Personal Presentation/Manner</li>
    <li><svg width="12" height="12" viewBox="0 0 12 12"><circle cx="6" cy="6" r="5" fill="none" stroke="#e6ad3b" stroke-width="1.3"/><path d="M3.5 6l1.8 1.8L8.6 4.3" fill="none" stroke="#e6ad3b" stroke-width="1.3"/></svg>Addressing and Overcoming Speaking/Communication Anxiety</li>
    <li><svg width="12" height="12" viewBox="0 0 12 12"><circle cx="6" cy="6" r="5" fill="none" stroke="#e6ad3b" stroke-width="1.3"/><path d="M3.5 6l1.8 1.8L8.6 4.3" fill="none" stroke="#e6ad3b" stroke-width="1.3"/></svg>Last-Minute Presentation 911</li>
    <li><svg width="12" height="12" viewBox="0 0 12 12"><circle cx="6" cy="6" r="5" fill="none" stroke="#e6ad3b" stroke-width="1.3"/><path d="M3.5 6l1.8 1.8L8.6 4.3" fill="none" stroke="#e6ad3b" stroke-width="1.3"/></svg>Media Training</li>
    <li><svg width="12" height="12" viewBox="0 0 12 12"><circle cx="6" cy="6" r="5" fill="none" stroke="#e6ad3b" stroke-width="1.3"/><path d="M3.5 6l1.8 1.8L8.6 4.3" fill="none" stroke="#e6ad3b" stroke-width="1.3"/></svg>Modifying Accents for Clarity and Intelligibility</li>
    <li><svg width="12" height="12" viewBox="0 0 12 12"><circle cx="6" cy="6" r="5" fill="none" stroke="#e6ad3b" stroke-width="1.3"/><path d="M3.5 6l1.8 1.8L8.6 4.3" fill="none" stroke="#e6ad3b" stroke-width="1.3"/></svg>Communicating Complex/Technical Material to Any Audience</li>
    <li><svg width="12" height="12" viewBox="0 0 12 12"><circle cx="6" cy="6" r="5" fill="none" stroke="#e6ad3b" stroke-width="1.3"/><path d="M3.5 6l1.8 1.8L8.6 4.3" fill="none" stroke="#e6ad3b" stroke-width="1.3"/></svg>Cultivating a More Effective Communication Style</li>
    <li><svg width="12" height="12" viewBox="0 0 12 12"><circle cx="6" cy="6" r="5" fill="none" stroke="#e6ad3b" stroke-width="1.3"/><path d="M3.5 6l1.8 1.8L8.6 4.3" fill="none" stroke="#e6ad3b" stroke-width="1.3"/></svg>Incorporating and Interacting with Audio/Visual Aids</li>
    <li><svg width="12" height="12" viewBox="0 0 12 12"><circle cx="6" cy="6" r="5" fill="none" stroke="#e6ad3b" stroke-width="1.3"/><path d="M3.5 6l1.8 1.8L8.6 4.3" fill="none" stroke="#e6ad3b" stroke-width="1.3"/></svg>Developing Tools for Dynamic Speaking</li>
    <li><svg width="12" height="12" viewBox="0 0 12 12"><circle cx="6" cy="6" r="5" fill="none" stroke="#e6ad3b" stroke-width="1.3"/><path d="M3.5 6l1.8 1.8L8.6 4.3" fill="none" stroke="#e6ad3b" stroke-width="1.3"/></svg>Conducting Communication 360° Interviews</li>
    <li><svg width="12" height="12" viewBox="0 0 12 12"><circle cx="6" cy="6" r="5" fill="none" stroke="#e6ad3b" stroke-width="1.3"/><path d="M3.5 6l1.8 1.8L8.6 4.3" fill="none" stroke="#e6ad3b" stroke-width="1.3"/></svg>Sharpening Presentation Skills for Attorneys</li>
  </ul>
  <div class="abs video" role="img" aria-label="Video still of a smiling coach giving speaking tips"></div>
  <svg class="abs play" width="50" height="50" viewBox="0 0 50 50"><circle cx="25" cy="25" r="22" fill="none" stroke="#fff" stroke-width="3"/><path d="M20 15l14 10-14 10z" fill="#fff"/></svg>
</section>

<footer>
  <div class="abs f-name">Hannah Brackwell</div>
  <div class="abs f-role">Public Speaking Consultant</div>
  <p class="abs f-text">Providing highly specialized executive coaching services and program design and facilitation for leadership development, public speaking, and all areas of spoken communication.</p>
  <a class="abs btn btn-blue f-contact">Contact Us</a>
  <div class="abs f-info"><span>e. info@brackwellvoicetutor.com</span><span>p. 718.555.0142</span></div>
  <div class="abs social f-social"><i></i><i class="on"></i><i></i><i></i><i></i></div>
  <a class="abs btn btn-gold f-reg">Register Now!</a>
  <svg class="abs to-top" width="28" height="28" viewBox="0 0 28 28"><path d="M4 24L14 4l10 20-10-6z" fill="none" stroke="#fff" stroke-width="2.2" stroke-linejoin="round"/></svg>
  <div class="abs footbar"><span class="c">© 2019 Brackwell Voice Tutoring</span><span class="l">Privacy Policy &nbsp; | &nbsp; Sitemap</span></div>
</footer>

</body>
</html>
```